Infographics about Quarnel Census

Hello, we are Plenvoria, a leading Big Data and Data Science consultancy firm from The Netherlands. We are looking for an awesome infographic.

Introduction
In order to create a better understanding of the status of Big Data in our little country, together with the biggest Big Data trade show Quarnel Fair, we created the Quarnel Census. This first national research on Big Data aims at providing insight in use of Big Data. The survey is built on five corner stones: Organization, Data, Technology, Skills and Process.

Design
We are looking for an insightful representation of the key-results of the survey, based on the five corner stones. It may also very well be multiple infographics in order to decrease the information density, but I'll leave that to you.

We are looking for a fresh, funky and attractive design, that is easily understood. Please use the colors (orange and blue) of the survey report. For more information see: http://www.plenvoria-example.com/static/images/quarnelcensus/quarnelcensus-uitkomst-web.pdf

```html
<!DOCTYPE html>
<html lang="en">
<head>
<meta charset="utf-8">
<title>Quarnel Census – Skills &amp; Process</title>
<link rel="stylesheet" href="https://fonts.googleapis.com/css2?family=Open+Sans:wght@400;600;700;800&family=Oswald:wght@500&display=swap">
<style>
:root{
  --blue:#2f78b8;
  --orange:#f7941d;
  --paper:#f4f4f2;
  --ink:#222;
  --badge:#555;
  --white:#fff;
  --rule:#9fb9d4;
  --seg-top:#e9a93a;
  --seg-right:#d3dce2;
  --seg-bottom:#d2e2da;
  --seg-left:#e2553a;
}
*{box-sizing:border-box;margin:0;padding:0}
html,body{width:1200px;height:2616px;overflow:hidden}
body{position:relative;font-family:"Open Sans",Arial,sans-serif;background:var(--white);color:var(--ink)}
.abs{position:absolute}

/* ---------- technology band ---------- */
.tech{position:absolute;left:0;top:0;width:1200px;height:401px;background:var(--blue);overflow:hidden;color:var(--white)}
.tech .ring{position:absolute;left:68px;top:16px}
.tech .mix{position:absolute;left:218px;top:2px;width:320px;font-size:21px;line-height:27px}
.tech .mix b{color:var(--orange);font-weight:700}
.tech .divider{position:absolute;left:602px;top:0;height:380px;border-left:3px dashed var(--rule)}
.tool{position:absolute;width:240px;height:64px;background:var(--white);border:3px solid var(--orange);border-radius:3px;display:flex;align-items:center}
.tool .pct{width:92px;text-align:center;font-size:32px;font-weight:800;color:var(--blue);border-right:3px solid var(--orange);height:100%;line-height:58px}
.tool .brand{flex:1;text-align:center;font-size:24px;font-weight:700;color:var(--badge)}

/* ---------- section heads ---------- */
.head{position:absolute;left:345px;width:506px;height:87px;background:var(--orange);color:var(--white);font-family:"Oswald",Impact,sans-serif;font-weight:500;font-size:62px;line-height:87px;text-align:center;letter-spacing:1px}

.num{position:absolute;width:72px;height:72px;border-radius:50%;background:var(--badge);border:6px solid var(--white);box-shadow:0 2px 6px rgba(0,0,0,.35);color:var(--white);font-weight:700;font-size:25px;line-height:60px;text-align:center}

/* ---------- skills ---------- */
.skills{position:absolute;left:0;top:401px;width:1200px;height:759px;background:var(--paper)}
.skills .divider{position:absolute;left:593px;top:139px;height:560px;border-left:3px dashed #bbb}
.q-title{position:absolute;font-size:29px;font-weight:700;line-height:37px;color:#333}
.grade{position:absolute;left:116px;top:430px;font-size:26px;line-height:34px;color:#333}
.grade b{font-weight:700}
.scale{position:absolute;left:113px;top:515px;display:flex;gap:8px}
.scale span{width:26px;height:26px;background:#d4d4d4}
.scale span.on{background:var(--orange)}
.stat{position:absolute;left:700px;display:flex;align-items:center}
.stat .dial{width:92px;height:92px;border-radius:50%;border:9px solid var(--orange);background:var(--white);color:var(--blue);font-weight:700;font-size:21px;line-height:74px;text-align:center;flex:none}
.stat p{margin-left:34px;font-size:23px;line-height:28px;color:#333;width:300px}

/* ---------- process ---------- */
.process{position:absolute;left:0;top:1160px;width:1200px;height:1299px;background:var(--blue);color:var(--white)}
.q-orange{position:absolute;color:var(--orange);font-weight:700}
.persona{position:absolute;left:532px;top:202px;width:362px;border-collapse:collapse}
.persona td{border-bottom:2px solid var(--rule);padding:10px 0;vertical-align:top;font-size:17px;line-height:21px}
.persona tr:last-child td{border-bottom:none}
.persona td.p{color:var(--orange);font-weight:800;font-size:24px;width:84px;line-height:24px}
.ethics{position:absolute;left:65px;width:300px;font-size:17px;line-height:21px}
.plan{position:absolute;left:860px;display:flex;align-items:flex-start;width:320px}
.plan b{color:var(--orange);font-size:24px;font-weight:800;width:60px;flex:none}
.plan span{font-size:17px;line-height:20px}
.plan.rule{border-bottom:2px solid var(--rule);padding-bottom:10px}
.usage{position:absolute;left:323px;top:1022px;width:666px;border-collapse:collapse;font-size:21px}
.usage th{text-align:left;font-weight:600;font-size:24px;padding:8px 10px;border-top:2px solid var(--white);border-bottom:2px solid var(--white)}
.usage td{padding:10px 10px;border-bottom:2px solid var(--rule)}
.usage td:first-child,.usage th:first-child{border-right:2px solid var(--white)}
.usage b{color:var(--orange);font-weight:800;font-size:25px;margin-right:14px}

/* ---------- footer ---------- */
.footer{position:absolute;left:0;top:2459px;width:1200px;height:157px;background:var(--white);display:flex;align-items:center;justify-content:space-around;padding:0 60px}
.mark{display:flex;align-items:center;gap:16px}
.mark i{display:block;width:46px;height:46px;background:var(--blue)}
.mark span{font-size:38px;font-weight:600;color:var(--blue)}
.mark small{display:block;font-size:13px;color:var(--orange);font-weight:600}
</style>
</head>
<body>

<section class="tech">
  <svg class="ring" width="160" height="160" viewBox="0 0 160 160" aria-hidden="true">
    <circle cx="80" cy="80" r="66" fill="var(--white)" stroke="#dcdcdc" stroke-width="16"/>
    <circle cx="80" cy="80" r="66" fill="none" stroke="var(--orange)" stroke-width="16" stroke-dasharray="187 415" transform="rotate(-90 80 80)"/>
    <text x="80" y="92" text-anchor="middle" font-family="Open Sans, sans-serif" font-weight="700" font-size="34" fill="var(--blue)">45%</text>
  </svg>
  <p class="mix">use a mix of <b>Open Source Software</b> &amp; <b>Licensed Software</b> the rest is divided equally between licensed software and open source</p>
  <div class="divider"></div>
  <div class="tool" style="left:640px;top:-18px"><span class="pct">21%</span><span class="brand">Hoplane</span></div>
  <div class="tool" style="left:916px;top:-18px"><span class="pct">10%</span><span class="brand">Pyrexa</span></div>
  <div class="tool" style="left:640px;top:119px"><span class="pct">8%</span><span class="brand">Sapto</span></div>
  <div class="tool" style="left:916px;top:119px"><span class="pct">7%</span><span class="brand">Stativo</span></div>
  <div class="tool" style="left:640px;top:258px"><span class="pct">6%</span><span class="brand">Saxel</span></div>
  <div class="tool" style="left:916px;top:258px"><span class="pct">7%</span><span class="brand">Rivan Studio</span></div>
</section>

<section class="skills">
  <div class="head" style="top:23px">SKILLS</div>
  <div class="divider"></div>

  <div class="num" style="left:60px;top:240px">01</div>
  <h3 class="q-title" style="left:166px;top:222px;width:380px">What Grade Would You Give The Level Of Knowledge Within Your Organization?</h3>
  <p class="grade">The <b>Average Grade</b> is a <b>6</b><br>on a scale of <b>10</b></p>
  <div class="scale"><span class="on"></span><span class="on"></span><span class="on"></span><span class="on"></span><span class="on"></span><span class="on"></span><span></span><span></span><span></span><span></span></div>

  <div class="num" style="left:679px;top:161px">02</div>
  <h3 class="q-title" style="left:788px;top:148px;width:380px">What Function Profiles Does Your Data Team Consist Of?</h3>
  <div class="stat" style="top:315px"><div class="dial">60%</div><p>Over 60% of organizations employ business analysts and/or data analysts</p></div>
  <div class="stat" style="top:456px"><div class="dial">38%</div><p>Only 38% of organizations employ data scientists</p></div>
  <div class="stat" style="top:594px"><div class="dial">17%</div><p>17% is planning to hire data scientists within the next year.</p></div>
</section>

<section class="process">
  <div class="head" style="top:19px">PROCESS</div>

  <div class="num" style="left:287px;top:159px">01</div>
  <h3 class="q-orange" style="left:227px;top:246px;width:300px;font-size:29px;line-height:35px">To what extent do you personalize your website?</h3>
  <table class="persona">
    <tr><td class="p">46%</td><td>Do not personalize its website</td></tr>
    <tr><td class="p">29%</td><td>Does this manually</td></tr>
    <tr><td class="p">15%</td><td>Personalizes based on historical data</td></tr>
    <tr><td class="p">11%</td><td>Are able to personalize the website in real-time based on current visitor behavior</td></tr>
  </table>

  <svg class="abs" style="left:362px;top:501px" width="480" height="480" viewBox="0 0 480 480" role="img" aria-label="Four-part cycle ring linking the process questions">
    <g fill="none" stroke-width="75" transform="rotate(-90 240 240)">
      <circle cx="240" cy="240" r="185" stroke="var(--seg-top)" stroke-dasharray="276 886" stroke-dashoffset="138"/>
      <circle cx="240" cy="240" r="185" stroke="var(--seg-right)" stroke-dasharray="276 886" stroke-dashoffset="-153"/>
      <circle cx="240" cy="240" r="185" stroke="var(--seg-bottom)" stroke-dasharray="276 886" stroke-dashoffset="-443"/>
      <circle cx="240" cy="240" r="185" stroke="var(--seg-left)" stroke-dasharray="276 886" stroke-dashoffset="-734"/>
    </g>
    <polygon points="240,0 210,28 270,28" fill="var(--seg-top)"/>
    <polygon points="480,240 452,210 452,270" fill="var(--seg-right)"/>
    <polygon points="240,480 210,452 270,452" fill="var(--seg-bottom)"/>
    <polygon points="0,240 28,210 28,270" fill="var(--seg-left)"/>
  </svg>

  <div class="num" style="left:173px;top:461px">02</div>
  <h3 class="q-orange" style="left:65px;top:555px;font-size:29px">Data ethics and value</h3>
  <p class="ethics" style="top:610px">Only 10% of participants think that consumers are well aware of the data trail they are leaving behind.</p>
  <p class="ethics" style="top:703px">Two third of all participants expects that in the future consumers can use data as a form of currency.</p>
  <p class="ethics" style="top:807px">Luckily, 82% of participants agrees that companies are responsible for collecting data ethically.</p>

  <div class="num" style="left:923px;top:452px">03</div>
  <h3 class="q-orange" style="left:851px;top:533px;width:340px;font-size:25px;line-height:31px">Are companies planning to use advanced methods, like deep learning, artificial intelligence and predictive models?</h3>
  <div class="plan rule" style="top:732px"><b>17%</b><span>Are already using these methods</span></div>
  <div class="plan" style="top:801px"><b>40%</b><span>Expects these methods to be in production within 3 years</span></div>

  <div class="num" style="left:220px;top:981px">04</div>
  <h3 class="q-orange" style="left:328px;top:958px;font-size:35px">What do you use data for?</h3>
  <table class="usage">
    <tr><th>TOP 3:</th><th>BOTTOM 3:</th></tr>
    <tr><td><b>19%</b>Marketing</td><td><b>3%</b>Human Resource</td></tr>
    <tr><td><b>16%</b>Online</td><td><b>4%</b>Finance and administration</td></tr>
    <tr><td><b>14%</b>Market analysis</td><td><b>5%</b>Supply chain &amp; Logistics</td></tr>
  </table>
</section>

<footer class="footer">
  <div class="mark"><i></i><div><span>Plenvoria</span><small>PROUDLY PART OF XENMAR GROUP</small></div></div>
  <div class="mark"><span>Quarnel Census</span></div>
  <div class="mark"><span>Quarnel Fair</span></div>
</footer>

</body>
</html>
```